Family Office for small businesses needs clear web site

I founded VORELTA Family Office, which is a french family office design to change the relationship between the customer and the wealth manager/insurance broker.
The main focus is : we give back to the client all the commissions / hidden costs we gain from the insurance companies / real estate builders and we bill to the client an annual fee proportional to the wealth. Thus a transparent relationship exempt from conflict of interest

I want a WORPRESS theme design that will be easily customizable in the future. Using and existing wordpress theme is not a problem, as long as i get to customize it in the future if necessary.
I want the web site to be Simple, clear, explaining the concepts detailed in the word doc i join to this project
In the chart are some of the things we do (not all, but most).
Also i joined some question a client might ask himself before calling us

i am available to clarify any issue or concepts
Updates

Target Market(s)

small businesses, specically their boss

Industry/Entity Type

Office

Number of Pages Required

1 page

Font styles to use
Serif

Colors
85acd3
3176b5
0455a3
cedeed
eaf1f7
cee9f5
85cae6
33a6d7
0692cd

Requirements
Must have
• I would like to have a one page wordpress theme personalized by a designer.
• I don't really care if you use an existing wordpress theme, as long as it can be upgraded/customized later on using wordpress/admin.
• I can even provide some themes I bought if it can help maintain the budget..
• O I can pay additional fee for a theme you bought to provide the design..

```html
<!DOCTYPE html>
<html lang="en">
<head>
<meta charset="utf-8">
<title>VORELTA Family Office</title>
<link rel="stylesheet" href="https://fonts.googleapis.com/css2?family=Open+Sans:wght@400;600;700;800&display=swap">
<style>
:root{
  --blue-light:#85acd3;
  --blue:#3176b5;
  --blue-deep:#0455a3;
  --blue-pale:#cedeed;
  --blue-mist:#eaf1f7;
  --sky:#33a6d7;
  --sky-strong:#0692cd;
  --ink:#1d2430;
  --text:#5d6673;
  --muted:#9aa2ad;
  --line:#e3e7ec;
  --band:#f4f5f7;
  --white:#fff;
}
*{box-sizing:border-box;margin:0;padding:0}
html,body{width:1200px;height:3368px;overflow:hidden}
body{font-family:"Open Sans",Arial,sans-serif;color:var(--text);background:var(--white);font-size:14px;line-height:1.6}
.wrap{width:1060px;margin:0 auto;position:relative}
a{color:var(--blue);text-decoration:none}
.arrow-link{font-size:13px;font-weight:600;color:var(--blue);display:inline-flex;align-items:center;gap:8px}
.arrow-link::after{content:"›";font-size:18px;line-height:1}

/* top bar */
.topbar{height:46px;background:var(--blue-deep);color:#dce8f4;font-size:12px}
.topbar .wrap{display:flex;align-items:center;height:46px;gap:30px}
.topbar .spacer{flex:1}
.topbar span{display:flex;align-items:center;gap:7px}
.topbar .cta{background:var(--sky-strong);color:#fff;height:46px;padding:0 22px;display:flex;align-items:center;font-weight:600}

/* header */
.header{height:84px;border-bottom:1px solid var(--line)}
.header .wrap{display:flex;align-items:center;height:84px}
.brand{display:flex;align-items:center;gap:12px;color:var(--ink);font-size:24px;font-weight:600;letter-spacing:.5px}
.brand i{width:14px;height:14px;background:var(--blue);display:block}
.brand small{font-size:10px;color:var(--muted);font-weight:400;line-height:1.2;width:80px;letter-spacing:0}
.nav{margin-left:auto;display:flex;gap:6px}
.nav a{padding:10px 20px;font-size:13px;color:var(--ink);font-weight:600}
.nav a.active{background:var(--blue);color:#fff}

/* hero */
.hero{padding-top:40px;height:560px}
.hero .wrap{height:500px}
.welcome{position:absolute;left:0;top:0;width:280px;height:400px;border:1px solid var(--line);padding:34px 30px;background:#fff;z-index:2}
.welcome h1{font-size:34px;font-weight:800;color:var(--ink);line-height:1.1;margin-bottom:14px}
.welcome p{font-size:12px;margin-bottom:22px}
.welcome ul{list-style:none;margin-bottom:40px}
.welcome li{font-size:14px;font-weight:600;color:var(--blue);padding:12px 0;border-bottom:1px solid var(--line);display:flex;gap:10px}
.welcome li::before{content:"›"}
.hero-photo{position:absolute;left:300px;top:0;width:760px;height:500px;background:linear-gradient(120deg,#eef1f4 0%,#d7dde4 55%,#aeb9c6 100%);border:1px solid var(--line)}
.hero-panel{position:absolute;right:0;top:260px;width:290px;height:240px;background:rgba(95,105,118,.85);color:#fff;padding:32px 28px}
.hero-panel h2{font-size:26px;font-weight:700;line-height:1.25;margin-bottom:24px}
.btn{display:inline-block;background:var(--sky-strong);color:#fff;font-size:13px;font-weight:600;padding:10px 22px}
.hero-panel .btn{position:absolute;right:28px;bottom:28px}

/* features */
.features{padding:60px 0 70px;text-align:center}
.features h2{font-size:30px;font-weight:700;color:var(--ink);margin-bottom:14px}
.features .lead{width:760px;margin:0 auto 54px;font-size:13px}
.feature-row{display:flex;justify-content:space-between;width:900px;margin:0 auto}
.feature{width:260px}
.feature svg{margin-bottom:12px}
.feature h3{font-size:14px;font-weight:700;color:var(--ink);margin-bottom:6px}
.feature p{font-size:12px}

.section-label{font-size:12px;font-weight:600;color:var(--ink);padding:12px 0;border-top:1px solid var(--line);margin-bottom:24px}

/* about */
.about{height:470px}
.about .col-left{position:absolute;left:0;top:60px;width:230px}
.big-title{font-size:38px;font-weight:800;color:var(--ink);line-height:1.12}
.about-photo{position:absolute;left:320px;top:0;width:470px;height:380px;background:linear-gradient(160deg,#c9ccd1 0%,#8d939c 50%,#3c4450 100%)}
.about-card{position:absolute;left:240px;top:110px;width:270px;height:210px;background:#fff;border:1px solid var(--line);padding:26px 24px;z-index:2}
.about-card h3{font-size:22px;font-weight:700;color:var(--ink);line-height:1.3;margin-bottom:14px}
.about-card p{font-size:12px}
.about .more{position:absolute;left:0;top:346px}
.stats{position:absolute;left:810px;top:0;width:250px}
.stat{border:1px solid var(--line);height:114px;padding:18px 22px;margin-bottom:16px}
.stat b{display:block;font-size:40px;font-weight:700;color:var(--blue);line-height:1.1}
.stat span{font-size:13px;color:var(--ink)}

/* methodology */
.method{height:460px;padding-top:10px}
.method .col-left{position:absolute;left:0;top:60px;width:330px}
.method .col-left p{font-size:12px;margin:14px 0 16px}
.steps{position:absolute;left:440px;top:110px;width:220px;text-align:right;list-style:none;border-right:2px solid var(--blue-pale);padding-right:18px}
.steps li{font-size:15px;font-weight:600;color:var(--blue);padding:6px 0}
.steps li.on{color:var(--blue-deep)}
.step-detail{position:absolute;left:690px;top:110px;width:370px;font-size:12px}
.step-detail h4{font-size:12px;color:var(--blue);font-weight:600;margin-bottom:6px}
.step-detail p{margin-bottom:12px}
.step-detail .small-link{font-size:11px;color:var(--ink);font-weight:600}
.method .next{position:absolute;right:0;top:390px;font-size:11px;color:var(--muted)}

/* testimonials */
.testimonials{background:var(--band);height:310px;text-align:center;padding-top:40px}
.testimonials .label{font-size:12px;font-weight:600;color:var(--ink);margin-bottom:30px}
.testimonials blockquote{width:760px;margin:0 auto 22px;font-size:24px;line-height:1.4;color:var(--ink);font-style:italic}
.testimonials cite{font-size:12px;color:var(--muted)}
.dots{margin-top:28px;display:flex;justify-content:center;gap:8px}
.dots i{width:7px;height:7px;border-radius:50%;background:#cfd4da}
.dots i.on{background:var(--blue)}

/* contact form */
.consult{text-align:center;padding-top:54px;height:510px}
.consult .label{font-size:12px;color:var(--muted)}
.consult h2{font-size:34px;font-weight:700;color:var(--ink);margin:4px 0 14px}
.consult .lead{width:760px;margin:0 auto 26px;font-size:12px}
.form{width:760px;margin:0 auto}
.form-row{display:flex;gap:16px;margin-bottom:16px}
.field{flex:1;height:42px;border:1px solid #d5dbe2;text-align:left;padding:11px 14px;font-size:12px;color:var(--muted)}
.field.select{border-color:var(--blue);color:var(--blue);display:flex;justify-content:space-between}
.field.area{height:130px}
.form .btn{margin-top:14px;padding:10px 38px}

/* footer */
.footer{border-top:1px solid var(--line);height:290px;padding-top:44px}
.footer .wrap{display:flex}
.f-col{width:530px}
.f-col h5{font-size:13px;color:var(--ink);font-weight:700;margin-bottom:20px}
.f-col .k{font-size:11px;color:var(--muted)}
.f-col .v{font-size:20px;color:var(--ink);margin-bottom:2px}
.f-col .arrow-link{font-size:11px;margin-bottom:20px}
.bottombar{border-top:1px solid var(--line);height:120px}
.bottombar .wrap{display:flex;height:60px;align-items:center;font-size:11px;color:var(--muted);gap:30px}
.bottombar .right{margin-left:auto}
</style>
</head>
<body>

<div class="topbar">
  <div class="wrap">
    <span><svg width="12" height="12" viewBox="0 0 24 24" fill="none" stroke="currentColor" stroke-width="2"><path d="M5 3h4l2 5-3 2a11 11 0 0 0 6 6l2-3 5 2v4a2 2 0 0 1-2 2A17 17 0 0 1 3 5a2 2 0 0 1 2-2z"/></svg>+33 1 42 60 18 35</span>
    <span><svg width="12" height="12" viewBox="0 0 24 24" fill="none" stroke="currentColor" stroke-width="2"><path d="M12 22s7-7 7-12a7 7 0 0 0-14 0c0 5 7 12 7 12z"/><circle cx="12" cy="10" r="2.5"/></svg>24, rue des Tilleuls 75008 Paris</span>
    <div class="spacer"></div>
    <a class="cta" href="#consult">Request a consultation</a>
  </div>
</div>

<header class="header">
  <div class="wrap">
    <div class="brand"><i></i>vorelta <small>Wealth management consultancy</small></div>
    <nav class="nav">
      <a class="active" href="#">Home</a><a href="#">About us</a><a href="#">Practice Areas</a><a href="#">Q&amp;A</a><a href="#">Contact</a>
    </nav>
  </div>
</header>

<section class="hero">
  <div class="wrap">
    <div class="welcome">
      <h1>Welcome.</h1>
      <p>We help business owners and their families shape and protect their wealth.</p>
      <ul>
        <li>Strategic consulting</li>
        <li>Operational Advice</li>
        <li>Family Counseling</li>
      </ul>
      <a class="arrow-link" href="#">Discover our services</a>
    </div>
    <div class="hero-photo" role="img" aria-label="Photo of a smiling consultant in shirt and tie working at a laptop in a bright office"></div>
    <div class="hero-panel">
      <h2>Make sure your objectives are being achieved.</h2>
      <a class="btn" href="#">Explore more</a>
    </div>
  </div>
</section>

<section class="features">
  <h2>Reliable and effective wealth management.</h2>
  <p class="lead">We offer a broad range of wealth planning products and services and can provide you with in-depth guidance to help you preserve your wealth and maximize growth potential.</p>
  <div class="feature-row">
    <div class="feature">
      <svg width="34" height="30" viewBox="0 0 34 30" fill="none" stroke="#3176b5" stroke-width="2"><path d="M4 28V18M12 28V12M20 28V16M28 28V6M2 28h30"/></svg>
      <h3>Boost your incomes</h3>
      <p>We are working to return every fee our partners pay to you, so your income grows with no hidden costs.</p>
    </div>
    <div class="feature">
      <svg width="34" height="30" viewBox="0 0 34 30" fill="none" stroke="#3176b5" stroke-width="2"><circle cx="11" cy="9" r="5"/><circle cx="24" cy="9" r="5"/><path d="M2 28c0-6 4-10 9-10s9 4 9 10M15 28c0-6 4-10 9-10s8 4 8 10"/></svg>
      <h3>Efficient collaboration</h3>
      <p>Our clients judge us on our efficiency above all, our ability to sustain their wealth over time.</p>
    </div>
    <div class="feature">
      <svg width="34" height="30" viewBox="0 0 34 30" fill="none" stroke="#3176b5" stroke-width="2"><rect x="4" y="3" width="26" height="25"/><path d="M10 11h14M10 17h14M10 23h8"/></svg>
      <h3>Simple process</h3>
      <p>We are available to our clients and stay beside them from the very first steps of each plan.</p>
    </div>
  </div>
</section>

<section class="about">
  <div class="wrap">
    <div class="section-label">About us</div>
    <div style="position:relative;height:400px">
      <div class="col-left">
        <h2 class="big-title">Meet<br>Vorelta.</h2>
      </div>
      <div class="about-photo" role="img" aria-label="Photo of the firm's founder in a suit standing on a staircase"></div>
      <div class="about-card">
        <h3>We are a family office based in Paris.</h3>
        <p>Our ambition is to become the trusted ally of families and their businesses. We only act in your interest.</p>
      </div>
      <a class="arrow-link more" href="#">Know more about Vorelta</a>
      <div class="stats">
        <div class="stat"><b>460</b><span>Happy clients</span></div>
        <div class="stat"><b>15</b><span>Consultants</span></div>
        <div class="stat"><b>2</b><span>Offices</span></div>
      </div>
    </div>
  </div>
</section>

<section class="method">
  <div class="wrap">
    <div class="section-label">Our methodology</div>
    <div style="position:relative;height:420px">
      <div class="col-left" style="top:0">
        <h2 class="big-title" style="font-size:32px">Independent.<br>Unbiased.<br>Honest.</h2>
        <p>Our process is the result of significant field research which, having been put into practice, ensures proper management of business so that you get results without wasting your time and money.</p>
        <a class="arrow-link" href="#">Know more about Vorelta</a>
      </div>
      <ul class="steps" style="top:40px">
        <li class="on">Discovery meeting</li>
        <li>Determine a plan</li>
        <li>Make a commitment</li>
        <li>Follow-up</li>
      </ul>
      <div class="step-detail" style="top:46px">
        <h4>First step</h4>
        <p>Request a consultation. We will arrange a meeting so we can discuss values, goals and current situation in order to establish written recommendations.</p>
        <p>During this step you will be invited to provide the following information:<br>— Personal information: name, phone, address…<br>— A report describing your financial current situation</p>
        <span class="small-link">Request a consultation</span>
      </div>
      <span class="next" style="top:300px">Move to next step ›</span>
    </div>
  </div>
</section>

<section class="testimonials">
  <div class="label">Testimonials</div>
  <blockquote>“ our consolidation and communication tools with the customers' very clear, overall performance management and asset class financial and nonfinancial ”</blockquote>
  <cite>Julien Marceau – Pharmacist</cite>
  <div class="dots"><i class="on"></i><i></i><i></i><i></i></div>
</section>

<section class="consult" id="consult">
  <div class="label">Get started</div>
  <h2>Request a consultation.</h2>
  <p class="lead">Please fill out the form below to receive a first consultation meeting arrangement. Required information are confidential and used only for consultation request. <b style="color:var(--ink)">We entirely respect your privacy.</b></p>
  <div class="form">
    <div class="form-row">
      <div class="field">Full name</div>
      <div class="field">Phone number</div>
      <div class="field select"><span>Real estate investment</span><span>⌄</span></div>
    </div>
    <div class="field area">Description</div>
    <a class="btn" href="#">SUBMIT</a>
  </div>
</section>

<footer class="footer">
  <div class="wrap">
    <div class="f-col">
      <h5>Where to find us</h5>
      <div class="k">Head office</div>
      <div class="v">24, rue des Tilleuls – 75008 Paris</div>
      <a class="arrow-link" href="#">Get directions on the map</a>
      <div class="k">Office</div>
      <div class="v">7, allée des Pins – 64200 Biarritz</div>
      <a class="arrow-link" href="#">Get directions on the map</a>
    </div>
    <div class="f-col">
      <h5>Contact</h5>
      <div class="k">Telephone</div>
      <div class="v">+33 1 42 60 18 35</div>
      <div class="v" style="margin-bottom:20px">+33 1 42 60 18 36</div>
      <div class="k">Drop us a line</div>
      <div class="v">contact@vorelta.fr</div>
    </div>
  </div>
</footer>

<div class="bottombar">
  <div class="wrap">
    <span>About us</span><span>Privacy policy</span><span>Legal Notice</span>
    <span class="right">© 2016 VORELTA Family Office. All Rights Reserved.</span>
  </div>
</div>

</body>
</html>
```